Oil Field Service company needs professional business cards

Looking to clean up our current company business cards and look a little more professional. Harlow Tubular Services is a US based company that services the oil field. We deal with engineers, managers and oil rigs....................................................................................................................................................................................................................................................................................................................................................................................................

Target Market(s)

Oil and Gas professionals

Industry/Entity Type

Oil And Gas

Contact Information for Business Card

See attached photo as example

Font styles to use
Sans Serif

Colors
ec1f27

Requirements
Must have
• Company Logo, Name, Title, Cell, Office, Fax, Email.
• See attached photo
Nice to have
• External CRT, Internal CRT, Casing Crews, Torque Turn, Laydown Machine
Should not have
• Do not introduce any new pictures and keep it professional looking

```html
<!DOCTYPE html>
<html lang="en">
<head>
<meta charset="utf-8">
<title>Harlow Tubular Services – Business Card</title>
<link rel="stylesheet" href="https://fonts.googleapis.com/css2?family=Open+Sans:wght@300;400;600;700&display=swap">
<style>
  :root {
    --red: #ec1f27;
    --slate: #4a5862;
    --slate-dark: #3d4952;
    --paper: #ffffff;
    --paper-shade: #eef0f1;
    --backdrop: #e6e3de;
    --muted: #b9c2c8;
  }
  * { box-sizing: border-box; margin: 0; padding: 0; }
  html, body {
    width: 1200px; height: 994px; overflow: hidden;
    background: var(--backdrop);
    font-family: "Open Sans", Arial, sans-serif;
  }
  .sheet {
    width: 1200px; height: 994px;
    display: flex; flex-direction: column; align-items: center; justify-content: center;
    gap: 60px;
  }
  .card {
    position: relative;
    width: 700px; height: 400px;
    background: linear-gradient(160deg, var(--paper) 55%, var(--paper-shade));
    overflow: hidden;
    box-shadow: 0 10px 28px rgba(0,0,0,.18);
  }
  .card svg.shapes { position: absolute; inset: 0; }

  /* contact side */
  .brand {
    position: absolute; right: 60px; top: 26px; text-align: right;
    color: var(--slate);
  }
  .brand-name { font-size: 62px; font-weight: 700; letter-spacing: 2px; line-height: 1; }
  .brand-tag { font-size: 16px; font-weight: 600; letter-spacing: 4px; line-height: 20px; margin-top: 6px; }

  .person { position: absolute; left: 40px; top: 196px; color: var(--paper); }
  .person-name { font-size: 24px; line-height: 1.1; }
  .person-name .first { font-weight: 300; color: var(--muted); }
  .person-name .last { font-weight: 600; }
  .person-title { font-size: 15px; color: var(--red); margin-top: 2px; }

  .contacts { position: absolute; left: 40px; top: 250px; list-style: none; }
  .contacts li {
    display: flex; align-items: center; gap: 12px;
    color: var(--paper); font-size: 14px; line-height: 16px; height: 17px;
  }
  .contacts svg { width: 13px; height: 13px; flex: none; }

  .services {
    position: absolute; left: 0; right: 0; top: 342px; height: 34px;
    display: flex; align-items: center; padding-left: 40px;
    color: var(--paper); font-size: 15px; letter-spacing: .3px;
  }
  .services span.sep { margin: 0 10px; }

  /* logo side */
  .reverse-mark {
    position: absolute; left: 0; right: 0; top: 0; bottom: 0;
    display: flex; align-items: center; justify-content: center;
    font-size: 120px; font-weight: 700; color: var(--slate); letter-spacing: 4px;
  }
</style>
</head>
<body>
<main class="sheet">

  <section class="card card-contact" aria-label="Contact side">
    <svg class="shapes" width="700" height="400" viewBox="0 0 700 400">
      <polygon points="0,180 700,146 700,400 0,400" fill="var(--slate)"/>
      <rect x="0" y="342" width="700" height="34" fill="var(--red)"/>
      <rect x="0" y="376" width="700" height="24" fill="var(--slate-dark)"/>
    </svg>

    <div class="brand">
      <div class="brand-name">HARLOW</div>
      <div class="brand-tag">TUBULAR SERVICES</div>
    </div>

    <div class="person">
      <div class="person-name"><span class="first">Wade</span> <span class="last">Carrington</span></div>
      <div class="person-title">Area Manager</div>
    </div>

    <ul class="contacts">
      <li>
        <svg viewBox="0 0 16 16"><path d="M3 1h3l1.5 4-2 1.3a9 9 0 0 0 4.2 4.2L11 8.5l4 1.5v3a2 2 0 0 1-2 2A12 12 0 0 1 1 3a2 2 0 0 1 2-2z" fill="var(--red)"/></svg>
        555 214-0700
      </li>
      <li>
        <svg viewBox="0 0 16 16"><rect x="4" y="1" width="8" height="14" rx="1.5" fill="none" stroke="var(--red)" stroke-width="1.6"/><circle cx="8" cy="12.5" r="1" fill="var(--red)"/></svg>
        555 382-1946
      </li>
      <li>
        <svg viewBox="0 0 16 16"><rect x="4" y="1" width="8" height="5" fill="var(--red)"/><rect x="1" y="6" width="14" height="6" rx="1" fill="var(--red)"/><rect x="4" y="10" width="8" height="5" fill="var(--paper)" stroke="var(--red)" stroke-width="1.2"/></svg>
        555 214-0731
      </li>
      <li>
        <svg viewBox="0 0 16 16"><path d="M8 1a5 5 0 0 1 5 5c0 4-5 9-5 9S3 10 3 6a5 5 0 0 1 5-5z" fill="var(--red)"/><circle cx="8" cy="6" r="1.8" fill="var(--slate)"/></svg>
        Redfield, OK 73100
      </li>
      <li>
        <svg viewBox="0 0 16 16"><rect x="1" y="3" width="14" height="10" rx="1" fill="var(--red)"/><path d="M1.5 3.8 8 9l6.5-5.2" fill="none" stroke="var(--slate)" stroke-width="1.3"/></svg>
        wcarrington@harlowtubular.com
      </li>
    </ul>

    <div class="services">
      Laydown Machine<span class="sep">|</span>Casing Crew<span class="sep">|</span>Mud Tool<span class="sep">|</span>Torque Turn
    </div>
  </section>

  <section class="card card-logo" aria-label="Logo side">
    <svg class="shapes" width="700" height="400" viewBox="0 0 700 400">
      <polygon points="0,0 70,0 0,120" fill="var(--red)"/>
      <polygon points="700,280 700,400 630,400" fill="var(--red)"/>
    </svg>
    <div class="reverse-mark">HARLOW</div>
  </section>

</main>
</body>
</html>
```